Business Card Design for Property Development Company Director

I am looking for a professional and unforgettable business card design for our Director of our Property Development Company.
Please see attached .pptx file to find out what information to include. You don't have to follow the exact format shown in the file - I am interested to see your creative flair using the information provided.

```html
<!DOCTYPE html>
<html lang="en">
<head>
<meta charset="utf-8">
<title>Halvard Property Group – Business Card</title>
<link href="https://fonts.googleapis.com/css2?family=Arimo:wght@400;700&display=swap" rel="stylesheet">
<style>
  :root {
    --backdrop: #2e2f31;
    --card: #f4f4f2;
    --brand-blue: #1f6fc0;
    --ink-grey: #5d5f62;
    --soft-grey: #7a7c7f;
  }
  * { box-sizing: border-box; margin: 0; padding: 0; }
  html, body { width: 1200px; height: 900px; overflow: hidden; }
  body {
    background: var(--backdrop);
    font-family: "Arimo", Arial, sans-serif;
    display: flex;
    align-items: center;
    justify-content: center;
    gap: 80px;
  }
  .card {
    width: 380px;
    height: 640px;
    background: var(--card);
    border-radius: 26px;
    position: relative;
    display: flex;
    flex-direction: column;
    align-items: center;
    text-align: center;
  }
  .brand {
    margin-top: 120px;
    display: flex;
    align-items: center;
    gap: 14px;
  }
  .brand-mark {
    width: 22px;
    height: 22px;
    background: var(--brand-blue);
  }
  .brand-name {
    color: var(--ink-grey);
    font-weight: 700;
    text-align: left;
    line-height: 1.05;
  }
  .brand-name .word { display: block; font-size: 44px; letter-spacing: 1px; }
  .brand-name .sub { display: block; font-size: 17px; letter-spacing: 4px; margin-top: 6px; }
  .person { margin-top: 110px; }
  .person-name {
    color: var(--brand-blue);
    font-weight: 700;
    font-size: 25px;
    letter-spacing: 1px;
  }
  .person-role {
    color: var(--ink-grey);
    font-size: 15px;
    letter-spacing: 1px;
    margin-top: 4px;
  }
  .contact-icons {
    display: flex;
    gap: 34px;
    margin-top: 26px;
  }
  .contact-icons svg { width: 32px; height: 32px; }
  .contact-lines {
    margin-top: 24px;
    color: var(--soft-grey);
    font-size: 19px;
    line-height: 1.75;
  }
  .dash {
    width: 20px;
    height: 4px;
    background: var(--brand-blue);
    margin: 18px auto;
  }
  .licence {
    color: var(--brand-blue);
    font-size: 17px;
    position: absolute;
    bottom: 34px;
    left: 0;
    right: 0;
  }
  .licence-dash { position: absolute; bottom: 64px; left: 180px; margin: 0; }
  .tagline {
    color: var(--brand-blue);
    font-weight: 700;
    font-size: 20px;
    line-height: 1.5;
  }
  .offer {
    position: absolute;
    bottom: 64px;
    left: 0;
    right: 0;
    font-size: 17px;
    color: var(--ink-grey);
    line-height: 1.35;
  }
  .offer strong { color: var(--brand-blue); font-weight: 700; }
</style>
</head>
<body>

  <section class="card card-front">
    <div class="brand">
      <span class="brand-mark"></span>
      <div class="brand-name">
        <span class="word">HALVARD</span>
        <span class="sub">PROPERTY GROUP</span>
      </div>
    </div>

    <div class="person">
      <h1 class="person-name">DANIEL MARLOW</h1>
      <p class="person-role">DIRECTOR</p>
    </div>

    <div class="contact-icons">
      <svg viewBox="0 0 32 32" aria-label="Phone">
        <circle cx="16" cy="16" r="16" fill="var(--brand-blue)"/>
        <path d="M9 13c0-2 2-3 7-3s7 1 7 3v1h-3v-1.5h-8V14H9z M11 15h10l2 7H9z" fill="#fff"/>
        <circle cx="16" cy="18.5" r="2" fill="var(--brand-blue)"/>
      </svg>
      <svg viewBox="0 0 32 32" aria-label="Email">
        <circle cx="16" cy="16" r="16" fill="var(--brand-blue)"/>
        <rect x="8.5" y="11" width="15" height="10" fill="#fff"/>
        <path d="M8.5 11l7.5 6 7.5-6" fill="none" stroke="var(--brand-blue)" stroke-width="1.4"/>
      </svg>
      <svg viewBox="0 0 32 32" aria-label="Website">
        <circle cx="16" cy="16" r="16" fill="var(--brand-blue)"/>
        <g fill="none" stroke="#fff" stroke-width="2" stroke-linecap="round">
          <path d="M14 19l-1.5 1.5a2.5 2.5 0 0 1-3.5-3.5L12 14a2.5 2.5 0 0 1 3.5 0"/>
          <path d="M18 13l1.5-1.5a2.5 2.5 0 0 1 3.5 3.5L20 18a2.5 2.5 0 0 1-3.5 0"/>
        </g>
      </svg>
    </div>

    <div class="contact-lines">
      <p>0400 118 236</p>
      <p>daniel@halvard.com.au</p>
      <p>www.halvard.com.au</p>
    </div>

    <div class="dash licence-dash"></div>
    <p class="licence">Real Estate Lic: 5127093 &amp; 5127094</p>
  </section>

  <section class="card card-back">
    <div class="brand">
      <span class="brand-mark"></span>
      <div class="brand-name">
        <span class="word">HALVARD</span>
        <span class="sub">PROPERTY GROUP</span>
      </div>
    </div>

    <div class="dash" style="margin-top:26px"></div>

    <p class="tagline">Property Development<br>&amp;<br>Site Acquisition Specialists</p>

    <div class="offer">
      <p>Ask me about our</p>
      <p><strong>INVESTMENT &amp; PARTNERSHIP</strong></p>
      <p>opportunities</p>
      <div class="dash"></div>
    </div>
  </section>

</body>
</html>
```